Pixel Perfect KRX9 style screens

From a high level, we have an existing app that is live in Tunevault. We are in the process of re-branding it to “Palmora” http://palmora-app.example and adding additional features. We have created the wireframe and mockup screens. This project is to create pixel perfect designs of the mock up screens provided, per the details in the word doc. We will accept a portion of the screens, if it includes the main jump screen and at least 4 of the other screens to establish an overall design style/look and feel. I am attaching our new logo. We want to keep the existing brand colors (Blue, Grey, and Orange), with updated logo, possibly making the blue more dominant than the orange (But up to designer), and new photo images. I am attaching one of the images that we are using on the website and in our marketing, but we need to add some additional ones for the new mobile home screen design, website, and marketing. We would like the style and fonts to match the new KRX9 font style guides (Fonts have been changed for KRX9), and everything should adhear to the KRX9 Human Interface guidelines published by quince. Please read the attached design spec doc and mock up screens for additional details.

Target Market(s)

Target Age: 18 - 35, Social Media / Dating

Industry/Entity Type

Social Club

Font styles to use
Other font styles liked:
• New KRX9 font: Marlow Text

Requirements
Must have
• It must conform to the KRX9 human interface guidelines, utilize the latest design elements, and will work on the multiple device sizes Target KRX7 and up, and zPad 5, 5s, 6, and 6plus. The screens must use the company colors, Blue, Orange, and gray:
• Orange: #ff9500
• Blue: #2aa9de
• Light Grey: #e5e5ea
• Medium Grey: #c7c7cc
• Dark Grey: #8e8e93
• White: #ffffff
Nice to have
• UI/UX improvements and recommendations

```html
<!DOCTYPE html>
<html lang="en">
<head>
<meta charset="utf-8">
<title>Palmora – KRX9 Screens</title>
<link rel="stylesheet" href="https://fonts.googleapis.com/css2?family=Inter:wght@400;500;600;700&display=swap">
<style>
:root{
  --orange:#ff9500;
  --blue:#2aa9de;
  --blue-deep:#1d8fc2;
  --grey-light:#e5e5ea;
  --grey-mid:#c7c7cc;
  --grey-dark:#8e8e93;
  --white:#ffffff;
  --ink:#3a3a3c;
  --page:#ffffff;
}
*{box-sizing:border-box;margin:0;padding:0}
html,body{width:1200px;height:2188px;overflow:hidden;background:var(--page);font-family:"Inter",sans-serif;color:var(--ink)}
.board{position:relative;width:1200px;height:2188px}
.label{position:absolute;width:338px;text-align:center;font-size:26px;font-weight:400;color:var(--ink)}
.screen{position:absolute;width:338px;height:600px;overflow:hidden;background:var(--blue);color:var(--white);display:flex;flex-direction:column;border-radius:6px}
.status{height:22px;display:flex;justify-content:space-between;align-items:center;padding:0 10px;font-size:10px;font-weight:600;flex:none}
.brand{display:flex;flex-direction:column;align-items:center;gap:6px}
.brand-dot{width:34px;height:34px;border-radius:50%;background:var(--white)}
.brand-name{font-size:18px;font-weight:600;color:var(--white)}
.brand.sm .brand-dot{width:22px;height:22px}
.brand.sm .brand-name{font-size:13px}
.photo{background:linear-gradient(160deg,#d9a777,#8a6a55 60%,#4d6f7e)}
.photo.cool{background:linear-gradient(160deg,#b9cbd6,#6d7f8c 60%,#3e4a55)}
.photo.warm{background:linear-gradient(160deg,#f1c79a,#b97e58 60%,#6a4a3c)}
.tabbar{height:58px;background:#dfe9ef;display:flex;flex:none}
.tab{flex:1;display:flex;align-items:center;justify-content:center;border-right:1px solid var(--grey-mid)}
.tab:last-child{border-right:none}
.tab svg{width:24px;height:24px;stroke:var(--grey-dark);fill:none;stroke-width:2}
.tab.active svg{stroke:var(--blue)}

/* splash */
.splash .brand{margin:auto}
.splash .brand-dot{width:60px;height:60px}
.splash .brand-name{font-size:26px}

/* login */
.login .brand{margin-top:60px}
.login-card{margin:30px 34px 0;background:var(--white);border-radius:4px;padding:14px;color:var(--ink)}
.seg{display:flex;border:1px solid var(--orange);border-radius:4px;overflow:hidden;margin-bottom:14px}
.seg span{flex:1;text-align:center;font-size:12px;padding:6px 0;color:var(--orange)}
.seg .on{background:var(--orange);color:var(--white)}
.field{height:28px;border:1px solid var(--grey-mid);border-radius:3px;margin-bottom:8px;font-size:11px;color:var(--grey-dark);padding:7px 8px}
.btn-orange{background:var(--orange);color:var(--white);font-size:12px;font-weight:600;text-align:center;padding:7px 0;border-radius:3px;width:60%;margin:6px auto 0}
.guest-btn{margin:20px auto 0;width:60%;background:var(--blue-deep);border:1px solid var(--white);border-radius:3px;font-size:11px;text-align:center;padding:7px 0}

/* loading */
.loading{position:relative}
.loading .backdrop{position:absolute;inset:0;background:linear-gradient(180deg,rgba(42,169,222,.85),rgba(42,169,222,.95)),linear-gradient(120deg,#d9a777,#5d7d8e)}
.loading .content{position:relative;display:flex;flex-direction:column;align-items:center;padding-top:60px;flex:1}
.loading h2{font-size:17px;font-weight:600;margin-top:24px}
.loading ul{list-style:none;margin-top:14px;font-size:11px;line-height:1.9;width:220px}
.loading li::before{content:"";display:inline-block;width:6px;height:6px;border-radius:50%;background:var(--white);margin-right:8px;vertical-align:middle}
.start{margin-top:36px;width:74px;height:74px;border-radius:50%;background:var(--white);border:4px solid var(--orange);display:flex;align-items:center;justify-content:center;font-size:12px;font-weight:700;color:var(--orange)}

/* hero screens */
.hero-top{height:80px;display:flex;align-items:center;justify-content:center;flex:none}
.hero-photo{flex:1;margin:0 18px 18px;position:relative;border:3px solid var(--white)}
.hero-caption{position:absolute;left:0;right:0;bottom:0;background:rgba(0,0,0,.35);text-align:center;font-size:16px;font-weight:500;padding:10px 0}

/* gender */
.gender .lead{text-align:center;font-size:15px;line-height:1.4;margin:10px 30px 16px}
.choice{margin:0 24px 14px;position:relative;height:170px;border:3px solid var(--white)}
.choice-label{position:absolute;left:0;right:0;bottom:0;background:rgba(42,169,222,.8);text-align:center;font-size:13px;font-weight:600;padding:7px 0}

/* grid */
.navbar{height:40px;display:flex;align-items:center;justify-content:space-between;padding:0 10px;flex:none}
.navbar svg{width:20px;height:20px;stroke:var(--white);fill:none;stroke-width:2}
.nav-icons{display:flex;gap:10px}
.grid{flex:1;background:var(--grey-light);display:grid;grid-template-columns:repeat(4,1fr);grid-auto-rows:1fr;gap:3px;padding:3px}
.tile{position:relative}
.tile::after{content:"";position:absolute;right:4px;bottom:4px;width:8px;height:8px;border-radius:50%;background:var(--orange);border:1px solid var(--white)}
.tile:nth-child(3n)::after{background:#4cd964}

/* looking for */
.looking{background:var(--white);color:var(--ink)}
.looking .status{background:var(--blue);color:var(--white)}
.look-head{background:var(--blue);padding:8px 12px 10px;display:flex;justify-content:space-between;align-items:center;flex:none}
.look-head .brand-name{font-size:13px}
.orange-band{background:var(--orange);color:var(--white);font-size:12px;font-weight:600;text-align:center;padding:7px 0;flex:none}
.profile{display:flex;flex-direction:column;align-items:center;padding:14px 0 10px}
.avatar{width:64px;height:64px;border-radius:50%;border:3px solid var(--blue);background:linear-gradient(160deg,#c9a88c,#6d5548)}
.profile-name{font-size:14px;font-weight:600;margin-top:6px}
.divider{height:1px;background:var(--grey-light);margin:0 16px}
.checks{display:grid;grid-template-columns:repeat(3,1fr);gap:10px 6px;padding:14px 20px;font-size:11px}
.checks span{display:flex;align-items:center;gap:5px}
.checks span::before{content:"";width:10px;height:10px;border:1px solid var(--grey-dark);border-radius:2px}
.checks .on::before{background:var(--blue);border-color:var(--blue)}
.rows{padding:6px 20px;font-size:11px;color:var(--grey-dark);display:flex;flex-direction:column;gap:10px}
.rows div{display:flex;justify-content:space-between;border-bottom:1px solid var(--grey-light);padding-bottom:6px}
.rows b{color:var(--ink);font-weight:500}
.btn-blue{margin:auto 60px 22px;background:var(--blue);color:var(--white);text-align:center;font-size:12px;font-weight:600;padding:8px 0;border-radius:3px}
</style>
</head>
<body>
<main class="board">

  <div class="label" style="left:31px;top:30px">Splash page</div>
  <div class="label" style="left:431px;top:30px">log-in page</div>
  <div class="label" style="left:831px;top:30px">loading</div>

  <section class="screen splash" style="left:31px;top:80px">
    <div class="status"><span>••••• Carrier</span><span>9:41 AM</span><span>100%</span></div>
    <div class="brand"><span class="brand-dot"></span><span class="brand-name">Palmora</span></div>
  </section>

  <section class="screen login" style="left:431px;top:80px">
    <div class="status"><span>••••• Carrier</span><span>9:41 AM</span><span>100%</span></div>
    <div class="brand"><span class="brand-dot"></span><span class="brand-name">Palmora</span></div>
    <div class="login-card">
      <div class="seg"><span class="on">Log In</span><span>Sign Up</span></div>
      <div class="field">Email</div>
      <div class="field">Password</div>
      <div class="btn-orange">Log In</div>
    </div>
    <div class="guest-btn">Log in as guest</div>
  </section>

  <section class="screen loading" style="left:831px;top:80px">
    <div class="backdrop" role="img" aria-label="Faded photo of friends together behind blue overlay"></div>
    <div class="status" style="position:relative"><span>••••• Carrier</span><span>9:41 AM</span><span>100%</span></div>
    <div class="content">
      <div class="brand"><span class="brand-dot"></span><span class="brand-name">Palmora</span></div>
      <h2>Start Finding Friends</h2>
      <ul>
        <li>Connect with people nearby</li>
        <li>Share interests and plans</li>
        <li>Meet new friends every day</li>
        <li>Chat safely and privately</li>
      </ul>
      <div class="start">START</div>
    </div>
  </section>

  <div class="label" style="left:31px;top:730px">Find New Friend</div>
  <div class="label" style="left:431px;top:730px">Gender Selection</div>
  <div class="label" style="left:831px;top:730px">Women</div>

  <section class="screen" style="left:31px;top:780px">
    <div class="status"><span>••••• Carrier</span><span>9:41 AM</span><span>100%</span></div>
    <div class="hero-top"><div class="brand sm"><span class="brand-dot"></span><span class="brand-name">Palmora</span></div></div>
    <div class="hero-photo photo warm" role="img" aria-label="Photo of two friends smiling together">
      <div class="hero-caption">Find New Friend</div>
    </div>
    <nav class="tabbar">
      <div class="tab active"><svg viewBox="0 0 24 24"><circle cx="12" cy="12" r="8"/><path d="M12 4v16M4 12h16"/></svg></div>
      <div class="tab"><svg viewBox="0 0 24 24"><path d="M12 20s-7-4.5-7-10a4 4 0 0 1 7-2.5A4 4 0 0 1 19 10c0 5.5-7 10-7 10z"/></svg></div>
      <div class="tab"><svg viewBox="0 0 24 24"><path d="M4 5h16v11H9l-5 4z"/></svg></div>
      <div class="tab"><svg viewBox="0 0 24 24"><circle cx="12" cy="8" r="4"/><path d="M4 21c1-5 15-5 16 0"/></svg></div>
    </nav>
  </section>

  <section class="screen gender" style="left:431px;top:780px">
    <div class="status"><span>••••• Carrier</span><span>9:41 AM</span><span>100%</span></div>
    <div class="hero-top" style="height:66px"><div class="brand sm"><span class="brand-dot"></span><span class="brand-name">Palmora</span></div></div>
    <p class="lead">I am interested<br>to connect with</p>
    <div class="choice photo warm" role="img" aria-label="Photo of a group of women"><div class="choice-label">Find New Friend</div></div>
    <div class="choice photo cool" role="img" aria-label="Photo of a group of men"><div class="choice-label">Find New Friend</div></div>
  </section>

  <section class="screen" style="left:831px;top:780px">
    <div class="status"><span>••••• Carrier</span><span>9:41 AM</span><span>100%</span></div>
    <div class="navbar">
      <svg viewBox="0 0 24 24"><path d="M3 6h18M3 12h18M3 18h18"/></svg>
      <div class="nav-icons">
        <svg viewBox="0 0 24 24"><path d="M12 20s-7-4.5-7-10a4 4 0 0 1 7-2.5A4 4 0 0 1 19 10c0 5.5-7 10-7 10z"/></svg>
        <svg viewBox="0 0 24 24"><path d="M4 5h16v11H9l-5 4z"/></svg>
      </div>
      <svg viewBox="0 0 24 24"><circle cx="11" cy="11" r="6"/><path d="M16 16l5 5"/></svg>
    </div>
    <div class="grid" role="img" aria-label="Grid of profile photos of women">
      <div class="tile photo warm"></div><div class="tile photo"></div><div class="tile photo warm"></div><div class="tile photo cool"></div>
      <div class="tile photo"></div><div class="tile photo warm"></div><div class="tile photo cool"></div><div class="tile photo warm"></div>
      <div class="tile photo warm"></div><div class="tile photo cool"></div><div class="tile photo"></div><div class="tile photo warm"></div>
      <div class="tile photo cool"></div><div class="tile photo warm"></div><div class="tile photo warm"></div><div class="tile photo"></div>
      <div class="tile photo"></div><div class="tile photo warm"></div><div class="tile photo cool"></div><div class="tile photo warm"></div>
      <div class="tile photo warm"></div><div class="tile photo"></div><div class="tile photo warm"></div><div class="tile photo cool"></div>
    </div>
  </section>

  <div class="label" style="left:31px;top:1430px">MEN</div>
  <div class="label" style="left:431px;top:1430px">Create Friend</div>
  <div class="label" style="left:831px;top:1430px">Looking for?</div>

  <section class="screen" style="left:31px;top:1480px">
    <div class="status"><span>••••• Carrier</span><span>9:41 AM</span><span>100%</span></div>
    <div class="navbar">
      <svg viewBox="0 0 24 24"><path d="M3 6h18M3 12h18M3 18h18"/></svg>
      <div class="nav-icons">
        <svg viewBox="0 0 24 24"><path d="M12 20s-7-4.5-7-10a4 4 0 0 1 7-2.5A4 4 0 0 1 19 10c0 5.5-7 10-7 10z"/></svg>
        <svg viewBox="0 0 24 24"><path d="M4 5h16v11H9l-5 4z"/></svg>
      </div>
      <svg viewBox="0 0 24 24"><circle cx="11" cy="11" r="6"/><path d="M16 16l5 5"/></svg>
    </div>
    <div class="grid" role="img" aria-label="Grid of profile photos of men">
      <div class="tile photo cool"></div><div class="tile photo"></div><div class="tile photo cool"></div><div class="tile photo warm"></div>
      <div class="tile photo"></div><div class="tile photo cool"></div><div class="tile photo warm"></div><div class="tile photo cool"></div>
      <div class="tile photo cool"></div><div class="tile photo warm"></div><div class="tile photo"></div><div class="tile photo cool"></div>
      <div class="tile photo warm"></div><div class="tile photo cool"></div><div class="tile photo cool"></div><div class="tile photo"></div>
      <div class="tile photo"></div><div class="tile photo cool"></div><div class="tile photo warm"></div><div class="tile photo cool"></div>
      <div class="tile photo cool"></div><div class="tile photo"></div><div class="tile photo cool"></div><div class="tile photo warm"></div>
    </div>
  </section>

  <section class="screen" style="left:431px;top:1480px">
    <div class="status"><span>••••• Carrier</span><span>9:41 AM</span><span>100%</span></div>
    <div class="hero-top"><div class="brand sm"><span class="brand-dot"></span><span class="brand-name">Palmora</span></div></div>
    <div class="hero-photo photo warm" role="img" aria-label="Photo of a smiling woman">
      <div class="hero-caption">Create Friendship Request</div>
    </div>
    <nav class="tabbar">
      <div class="tab"><svg viewBox="0 0 24 24"><circle cx="12" cy="12" r="8"/><path d="M12 4v16M4 12h16"/></svg></div>
      <div class="tab active"><svg viewBox="0 0 24 24"><path d="M9 18V5l10-2v13"/><circle cx="7" cy="18" r="2"/><circle cx="17" cy="16" r="2"/></svg></div>
      <div class="tab"><svg viewBox="0 0 24 24"><path d="M4 5h16v11H9l-5 4z"/></svg></div>
      <div class="tab"><svg viewBox="0 0 24 24"><circle cx="12" cy="8" r="4"/><path d="M4 21c1-5 15-5 16 0"/></svg></div>
    </nav>
  </section>

  <section class="screen looking" style="left:831px;top:1480px">
    <div class="status"><span>••••• Carrier</span><span>9:41 AM</span><span>100%</span></div>
    <div class="look-head">
      <svg width="18" height="18" viewBox="0 0 24 24" fill="none" stroke="#fff" stroke-width="2"><path d="M3 6h18M3 12h18M3 18h18"/></svg>
      <div class="brand sm" style="flex-direction:row"><span class="brand-name">Palmora</span></div>
      <svg width="18" height="18" viewBox="0 0 24 24" fill="none" stroke="#fff" stroke-width="2"><circle cx="11" cy="11" r="6"/><path d="M16 16l5 5"/></svg>
    </div>
    <div class="orange-band">What are you interested in?</div>
    <div class="profile">
      <div class="avatar" role="img" aria-label="Profile photo"></div>
      <div class="profile-name">Dale Morrow</div>
    </div>
    <div class="divider"></div>
    <div class="checks">
      <span class="on">Coffee</span><span>Movies</span><span class="on">Hiking</span>
      <span>Music</span><span class="on">Travel</span><span>Gaming</span>
      <span>Sports</span><span>Dining</span><span class="on">Books</span>
    </div>
    <div class="rows">
      <div>Age range <b>18 - 35</b></div>
      <div>Distance <b>10 mi</b></div>
    </div>
    <div class="btn-blue">Save</div>
  </section>

</main>
</body>
</html>
```